CREATE A BUSINESS CARD FOR A BOAT CLEANING SERVICE

WE ARE STARTING A NEW BOAT CLEANING BUSINESS. WE DIVE UNDERWATER TO CLEAN BOAT HULLS, JETTIES, UNDERWATER STRUCTURES ETC. WE ARE LOOKING FOR AN UPPERMARKET MODERN LOGO AND BUSINESS CARD AS ALOT OF OUR TARGET MARKET WILL BE HIGH END. YOU HAVE TO DESIGN A BUSINESS CARD AND LOGO SEPERATELY .
THE BUSINESS CARD DIMESNION MUST BE STANDARD SIZE.
The standard dimensions of a printed business card are 3.5 x 2 inches

Target Market(s)

UNDERWATER SERVICED

Industry/Entity Type

Business

Contact Information for Business Card

HALDEN UNDERWATER SERVICES

Font styles to use
Serif

Colors

Designer to choose colors to be used in the design.

Requirements
Must have
• HALDEN
Nice to have
• dark
Should not have
• more than 3 colors

```html
<!DOCTYPE html>
<html lang="en">
<head>
<meta charset="utf-8">
<title>Halden Underwater Services – Business Cards</title>
<link rel="stylesheet" href="https://fonts.googleapis.com/css2?family=Open+Sans:wght@400;600;700&display=swap">
<style>
  :root {
    --navy: #144f8c;
    --grey: #a3a3a3;
    --white: #ffffff;
    --stage: #eceae6;
    --ink-grey: #7d7d7d;
  }
  * { margin: 0; padding: 0; box-sizing: border-box; }
  html, body { width: 1200px; height: 900px; overflow: hidden; }
  body {
    background: var(--stage);
    font-family: "Open Sans", Arial, sans-serif;
    position: relative;
  }
  .card {
    position: absolute;
    overflow: hidden;
    box-shadow: 0 6px 18px rgba(0,0,0,0.18);
  }
  /* Front */
  .card-front {
    left: 78px; top: 35px; width: 587px; height: 362px;
    background: var(--grey);
    color: var(--white);
  }
  .card-front .wave { position: absolute; inset: 0; }
  .card-front .person { position: absolute; left: 30px; top: 44px; }
  .person-name { font-size: 20px; font-weight: 700; letter-spacing: 0.3px; line-height: 1.1; }
  .person-role { font-size: 16px; font-weight: 400; margin-top: 2px; }
  .contact-list {
    position: absolute; left: 30px; top: 108px; list-style: none;
    font-size: 15.5px; line-height: 21.5px;
  }
  .contact-list li { display: flex; align-items: center; gap: 8px; }
  .contact-list svg { width: 11px; height: 11px; fill: var(--white); flex: none; }
  .address {
    position: absolute; left: 30px; top: 290px;
    font-size: 15.5px; line-height: 22px;
  }
  .wordmark {
    position: absolute; text-align: center; font-weight: 600; line-height: 1;
  }
  .wordmark .wm-main { display: block; letter-spacing: 1px; }
  .wordmark .wm-sub { display: block; letter-spacing: 2.4px; }
  .card-front .wordmark { right: 36px; top: 278px; color: var(--white); }
  .card-front .wm-main { font-size: 44px; }
  .card-front .wm-sub { font-size: 12.5px; margin-top: 4px; }

  /* Back */
  .card-back {
    left: 388px; top: 505px; width: 567px; height: 352px;
    background: var(--white);
  }
  .card-back .wordmark {
    left: 0; right: 0; top: 156px; color: var(--navy);
  }
  .card-back .wm-main { font-size: 46px; }
  .card-back .wm-sub { font-size: 13px; margin-top: 5px; }
  .service-band {
    position: absolute; left: 0; right: 0; top: 250px; height: 70px;
    background: var(--navy); color: var(--white);
    display: flex; flex-direction: column; justify-content: center; align-items: center;
    font-size: 14px; font-weight: 600; line-height: 19px; letter-spacing: 0.2px;
    text-transform: uppercase;
  }
</style>
</head>
<body>

<section class="card card-front" aria-label="Business card front">
  <svg class="wave" viewBox="0 0 587 362" preserveAspectRatio="none" aria-hidden="true">
    <path d="M0,292 C60,222 150,182 300,186 C420,190 505,150 587,78 L587,362 L0,362 Z" fill="var(--navy)"/>
  </svg>
  <div class="person">
    <p class="person-name">MARCUS ELLERY</p>
    <p class="person-role">Managing Director</p>
  </div>
  <ul class="contact-list">
    <li><svg viewBox="0 0 24 24"><path d="M6.6 10.8a15.1 15.1 0 0 0 6.6 6.6l2.2-2.2c.3-.3.7-.4 1-.2 1.1.4 2.3.6 3.6.6.6 0 1 .4 1 1V20c0 .6-.4 1-1 1A17 17 0 0 1 3 4c0-.6.4-1 1-1h3.5c.6 0 1 .4 1 1 0 1.3.2 2.5.6 3.6.1.3 0 .7-.2 1z"/></svg>(044)987650321</li>
    <li><svg viewBox="0 0 24 24"><path d="M2 5h20v14H2z M2 5l10 8 10-8" fill="var(--white)"/><path d="M3 6.5l9 7 9-7" fill="none" stroke="var(--grey)" stroke-width="2"/></svg>hello@haldenunderwater.com</li>
    <li><svg viewBox="0 0 24 24"><circle cx="12" cy="12" r="10"/><path d="M2 12h20M12 2c3 3 3 17 0 20M12 2c-3 3-3 17 0 20" fill="none" stroke="var(--grey)" stroke-width="1.6"/></svg>www.haldenunderwater.com</li>
  </ul>
  <p class="address">18 Harbour Quay Road,<br>Marina Bay, 40721</p>
  <div class="wordmark">
    <span class="wm-main">HALDEN</span>
    <span class="wm-sub">UNDERWATER SERVICES</span>
  </div>
</section>

<section class="card card-back" aria-label="Business card back">
  <div class="wordmark">
    <span class="wm-main">HALDEN</span>
    <span class="wm-sub">UNDERWATER SERVICES</span>
  </div>
  <div class="service-band">
    <span>We dive underwater to clean boat hulls</span>
    <span>jetties, underwater structures etc</span>
  </div>
</section>

</body>
</html>
```